1/4 page magazine ad

We would like a 1/4 ad in a magazine advertising a doctor in our practice. Dr. Lena Moskit, DC is the only Female Haldrup Certified chiropractor in Williamsburg, VA. We would like the ad to include a large eye catching picture of a woman's pregnant belly, as the Haldrup technique is for pregnant women. Please take a look at our previous ad that we have had done to see some of the elements that we liked in our other ad.

```html
<!DOCTYPE html>
<html lang="en">
<head>
<meta charset="utf-8">
<title>Colonial Spine &amp; Posture Center – Quarter Page Ad</title>
<link href="https://fonts.googleapis.com/css2?family=Bebas+Neue&family=Oswald:wght@500;600;700&family=Arimo:wght@400;700&display=swap" rel="stylesheet">
<style>
  :root {
    --page-bg: #f2f2f2;
    --paper: #ffffff;
    --brand-red: #7d0000;
    --brand-yellow: #f7bd1d;
    --ink: #111111;
    --logo-grey: #6d6d6d;
    --belly-pink: #e8307a;
    --belly-deep: #c41a5c;
    --belly-light: #f26a9f;
  }
  * { box-sizing: border-box; margin: 0; padding: 0; }
  html, body {
    width: 1200px; height: 1200px; overflow: hidden;
    background: var(--page-bg);
  }
  .ad {
    position: absolute; left: 180px; top: 74px;
    width: 848px; height: 1059px;
    background: var(--paper);
    overflow: hidden;
    box-shadow: 0 6px 18px rgba(0,0,0,0.25);
  }
  .hero-photo {
    position: absolute; left: 575px; top: 0; width: 273px; height: 958px;
    background: linear-gradient(160deg, var(--belly-light) 0%, var(--belly-pink) 50%, var(--belly-deep) 100%);
  }

  .brand { position: absolute; left: 55px; top: 54px; display: flex; align-items: center; gap: 16px; }
  .brand-mark { width: 106px; height: 117px; background: var(--logo-grey); }
  .brand-name {
    font-family: "Oswald", sans-serif; font-weight: 600;
    color: var(--brand-red); font-size: 38px; line-height: 1.12;
    letter-spacing: 1px; text-transform: uppercase;
  }

  .doctor-photo {
    position: absolute; left: 53px; top: 236px; width: 170px; height: 223px;
    border: 2px solid #666;
    background: linear-gradient(160deg, #6f8d48 0%, #8a6a4a 45%, #3a2a22 75%, #1f2e55 100%);
  }
  .welcome {
    position: absolute; left: 228px; top: 246px;
    font-family: "Bebas Neue", sans-serif; font-weight: 400;
    color: var(--brand-red); font-size: 104px; line-height: 102px;
    text-transform: uppercase; letter-spacing: 0;
  }

  .rule { position: absolute; left: 0; height: 3px; background: var(--brand-yellow); }
  .rule--top { top: 472px; width: 486px; }
  .rule--bottom { top: 572px; width: 466px; }

  .name-banner {
    position: absolute; left: 0; top: 483px; width: 464px; height: 80px;
    background: var(--brand-red);
  }
  .name-banner h1 {
    position: absolute; left: 53px; top: 4px;
    font-family: "Oswald", sans-serif; font-weight: 600;
    color: #fff; font-size: 52px; line-height: 70px; letter-spacing: -0.5px;
  }

  .tagline {
    position: absolute; left: 53px; top: 588px; width: 400px;
    font-family: "Arimo", sans-serif; font-size: 28px; line-height: 41px; color: var(--ink);
  }

  .appointment-tab { position: absolute; left: 0; top: 722px; width: 360px; height: 60px; }
  .appointment-tab span {
    position: absolute; left: 53px; top: 8px;
    font-family: "Oswald", sans-serif; font-weight: 600;
    color: #fff; font-size: 28px; line-height: 40px;
  }

  .phone-band {
    position: absolute; left: 0; top: 784px; width: 476px; height: 79px;
    background: var(--brand-yellow);
    display: flex; align-items: center; padding-left: 53px; gap: 16px;
  }
  .phone-band svg { width: 50px; height: 50px; }
  .phone-number {
    font-family: "Oswald", sans-serif; font-weight: 700;
    font-size: 58px; line-height: 1; color: var(--ink);
  }

  .address {
    position: absolute; left: 53px; top: 880px;
    font-family: "Arimo", sans-serif; font-size: 23px; line-height: 35px; color: var(--ink);
  }

  .footer {
    position: absolute; left: 0; top: 958px; width: 848px; height: 101px;
    background: var(--brand-red);
  }
  .website {
    position: absolute; left: 0; right: 0; top: 16px; text-align: center;
    font-family: "Arimo", sans-serif; font-weight: 700;
    font-size: 25px; letter-spacing: 3px; color: #fff;
  }
  .website .domain { color: var(--brand-yellow); }
</style>
</head>
<body>
  <div class="ad">
    <div class="hero-photo" role="img" aria-label="Photo of a pregnant woman in a pink top cradling her belly with both hands"></div>

    <div class="brand">
      <div class="brand-mark"></div>
      <div class="brand-name">Colonial<br>Spine &amp; Posture<br>Center</div>
    </div>

    <div class="doctor-photo" role="img" aria-label="Portrait of Dr. Lena Moskit smiling"></div>
    <div class="welcome">Welcome<br>Back!</div>

    <div class="rule rule--top"></div>
    <div class="name-banner"><h1>Dr. Lena Moskit, DC</h1></div>
    <div class="rule rule--bottom"></div>

    <p class="tagline">The only Female Haldrup Certified chiropractor in Williamsburg, VA.</p>

    <div class="appointment-tab">
      <svg width="360" height="60" viewBox="0 0 360 60" aria-hidden="true">
        <path d="M0 0 H322 Q332 0 337 8 L360 60 H0 Z" fill="var(--brand-red)"/>
      </svg>
      <span>Make an Appointment:</span>
    </div>

    <div class="phone-band">
      <svg viewBox="0 0 50 50" aria-hidden="true">
        <path d="M12 6 L19 15 Q21 18 18 21 L16 23 Q20 31 27 34 L29 32 Q32 29 35 31 L44 38 Q46 40 44 43 L40 47 Q36 50 28 46 Q12 38 4 22 Q0 14 3 10 L7 6 Q10 4 12 6 Z" fill="var(--ink)"/>
        <path d="M28 12 Q37 14 38 23" stroke="var(--ink)" stroke-width="3" fill="none" stroke-linecap="round"/>
        <path d="M29 5 Q44 8 45 22" stroke="var(--ink)" stroke-width="3" fill="none" stroke-linecap="round"/>
      </svg>
      <span class="phone-number">757-555-0148</span>
    </div>

    <p class="address">2215 Tavern Lane, # 310,<br>Williamsburg, VA 23188</p>

    <div class="footer">
      <p class="website">www.<span class="domain">colonialspineandposture</span>.com</p>
    </div>
  </div>
</body>
</html>
```